Ironbark Shift Workforce

We are a underground coal mining labour hire company, needing a website that links into our online payroll (www.wagetrackly.com.au) and also need to have job applications page that is a preform with drop down menu,s with answers or check boxes. We would also need a 3 tier administration access for access to different files.
We are looking for an ongoing relationship with future app integration

Reason: There are a few more designs to come and I'm out at the mine for another week

Industry/Entity Type

Coal Mining

```html
<!DOCTYPE html>
<html lang="en">
<head>
<meta charset="utf-8">
<title>Ironbark Shift Workforce — Application for Position</title>
<link rel="stylesheet" href="https://fonts.googleapis.com/css2?family=PT+Sans:wght@400;700&family=Roboto+Slab:wght@300&family=Arimo:wght@400;700&display=swap">
<style>
  :root {
    --bar-dark: #1c1c1c;
    --bar-light: #2b2b2b;
    --page-bg: #f4f4f4;
    --panel-bg: #fbfbfb;
    --panel-head: #ececec;
    --line: #e6e6e6;
    --field-border: #d2d2d2;
    --ink: #1e1e1e;
    --ink-soft: #555555;
    --ink-faint: #9a9a9a;
    --nav-text: #e9e9e9;
    --accent: #f0600e;
    --accent-dark: #d04c05;
    --button-blue: #4a9ad8;
    --photo-dark: #3a2e1c;
    --photo-mid: #7a6232;
    --photo-light: #c9a94a;
  }
  * { box-sizing: border-box; margin: 0; padding: 0; }
  html, body { width: 875px; height: 1200px; overflow: hidden; }
  body {
    position: relative;
    background: radial-gradient(ellipse at 50% 20%, #ffffff 0%, var(--page-bg) 60%, #ededed 100%);
    font-family: "Arimo", Arial, sans-serif;
    color: var(--ink);
  }

  /* Header */
  .site-header {
    position: absolute; left: 0; top: 0; width: 875px; height: 62px;
    background: linear-gradient(var(--bar-light), var(--bar-dark));
  }
  .brand {
    position: absolute; left: 109px; top: 11px;
    display: flex; align-items: center; gap: 8px;
    font-family: "PT Sans", sans-serif; font-weight: 400; font-size: 30px; color: #ffffff;
    letter-spacing: 1px;
  }
  .brand-dot { width: 40px; height: 40px; border-radius: 50%; border: 3px solid #ffffff; }
  .main-nav {
    position: absolute; right: 109px; top: 25px;
    display: flex; gap: 30px;
    font-family: "PT Sans", sans-serif; font-weight: 700; font-size: 11px;
    color: var(--nav-text); text-transform: uppercase;
  }

  /* Hero */
  .hero {
    position: absolute; left: 109px; top: 82px; width: 657px; height: 236px;
    background: linear-gradient(90deg, #e8e4dc, #f6f5f2);
    border: 1px solid #dcdcdc; overflow: hidden;
  }
  .hero-photo { position: absolute; left: 0; top: 0; }
  .hero-copy {
    position: absolute; left: 380px; top: 56px; width: 240px; text-align: center;
  }
  .hero-title { font-family: "PT Sans", sans-serif; font-weight: 700; font-size: 22px; color: var(--ink); }
  .hero-sub { font-family: "Roboto Slab", serif; font-weight: 300; font-size: 21px; line-height: 25px; color: #333; margin-top: 8px; }
  .hero-button {
    display: inline-flex; align-items: center; gap: 8px;
    margin-top: 14px; padding: 7px 10px 7px 12px;
    background: linear-gradient(#fafafa, #dcdcdc); border: 1px solid #bdbdbd; border-radius: 2px;
    font-family: "PT Sans", sans-serif; font-weight: 700; font-size: 11px; color: #333; text-transform: uppercase;
  }

  /* Welcome */
  .welcome { position: absolute; left: 109px; top: 334px; width: 657px; }
  .welcome h1 { font-family: "PT Sans", sans-serif; font-weight: 700; font-size: 16px; color: var(--ink); }
  .welcome p { margin-top: 6px; font-family: "PT Sans", sans-serif; font-size: 10.5px; line-height: 15px; color: var(--ink-soft); }

  /* Application panel */
  .application {
    position: absolute; left: 109px; top: 434px; width: 657px; height: 704px;
    background: var(--panel-bg); border: 1px solid #e0e0e0;
    box-shadow: 0 1px 3px rgba(0,0,0,0.08);
  }
  .application-head {
    height: 36px; background: var(--panel-head); border-bottom: 1px solid #dedede;
    padding: 10px 0 0 16px;
    font-family: "PT Sans", sans-serif; font-weight: 700; font-size: 16px; color: var(--ink);
  }
  .question { position: absolute; left: 21px; width: 615px; }
  .question + .divider { }
  .divider { position: absolute; left: 0; width: 655px; height: 1px; background: var(--line); }
  .q-label { font-size: 10.5px; font-weight: 700; color: var(--ink); }
  .text-field {
    width: 399px; height: 26px; margin-top: 6px;
    background: #ffffff; border: 1px solid var(--field-border); border-radius: 3px;
    position: relative;
  }
  .text-field::after {
    content: ""; position: absolute; right: 3px; bottom: 3px; width: 5px; height: 5px;
    border-right: 1px dotted #999; border-bottom: 1px dotted #999;
  }
  .choices { display: flex; flex-wrap: wrap; gap: 0 14px; margin-top: 7px; }
  .choice { display: flex; align-items: center; gap: 4px; font-size: 9.5px; color: var(--ink-faint); }
  .box { width: 9px; height: 9px; border: 1px solid #b5b5b5; background: #fff; border-radius: 1px; }
  .q-note { margin-top: 5px; font-size: 8px; color: #b0b0b0; }
  .inline-row { display: flex; align-items: center; justify-content: space-between; width: 399px; }
  .select-field {
    width: 47px; height: 20px; background: #fff; border: 1px solid var(--field-border); border-radius: 3px;
    display: flex; align-items: center; justify-content: space-between; padding: 0 5px 0 14px;
    font-size: 9px; color: var(--ink);
  }
  .phone-row { display: flex; gap: 8px; margin-top: 6px; }
  .phone-field { height: 26px; background: #fff; border: 1px solid var(--field-border); border-radius: 3px; font-size: 9.5px; color: var(--ink-faint); display: flex; align-items: center; justify-content: center; }
  .submit-button {
    position: absolute; left: 21px; top: 658px;
    display: inline-flex; align-items: center; gap: 5px;
    height: 23px; padding: 0 8px;
    background: linear-gradient(var(--accent), var(--accent-dark)); border-radius: 2px;
    font-size: 10.5px; font-weight: 700; color: #fff;
  }

  /* Footer */
  .site-footer {
    position: absolute; left: 0; top: 1166px; width: 875px; height: 34px;
    background: var(--bar-dark); color: #f0f0f0; font-size: 9.5px;
  }
  .copyright { position: absolute; left: 109px; top: 12px; }
  .footer-nav { position: absolute; right: 109px; top: 12px; display: flex; gap: 10px; }
</style>
</head>
<body>

<header class="site-header">
  <div class="brand"><span class="brand-dot"></span>ISW</div>
  <nav class="main-nav">
    <span>Home</span><span>About Us</span><span>Mission Statement</span><span>Contact Us</span>
  </nav>
</header>

<section class="hero">
  <svg class="hero-photo" width="380" height="236" viewBox="0 0 380 236" role="img" aria-label="Photo of an underground coal miner standing beside mining machinery">
    <defs>
      <linearGradient id="mineTones" x1="0" y1="0" x2="1" y2="1">
        <stop offset="0" stop-color="#5b4a2a"/>
        <stop offset="0.45" stop-color="var(--photo-light)"/>
        <stop offset="0.75" stop-color="var(--photo-mid)"/>
        <stop offset="1" stop-color="var(--photo-dark)"/>
      </linearGradient>
    </defs>
    <path d="M0 0 H326 Q380 118 326 236 H0 Z" fill="url(#mineTones)"/>
    <path d="M326 0 Q380 118 326 236" fill="none" stroke="#e8d9a8" stroke-width="2"/>
  </svg>
  <div class="hero-copy">
    <div class="hero-title">Lorem ipsum dolor amet</div>
    <div class="hero-sub">Donec sit amet fringilla tortor Morbi</div>
    <div class="hero-button">Get Started
      <svg width="16" height="16" viewBox="0 0 16 16"><circle cx="8" cy="8" r="7.5" fill="var(--button-blue)"/><path d="M6 4.5 L11 8 L6 11.5 Z" fill="#fff"/></svg>
    </div>
  </div>
</section>

<section class="welcome">
  <h1>Welcome to Ironbark Shift</h1>
  <p>Lorem ipsum dolor sit amet, consectetur adipiscing elit. Proin a gravida sapien, vitae varius dui. In rutrum egestas magna. Fusce eu ante dignissim mi rutrum pretium sit amet quis massa. Nulla pharetra pretium libero, vitae tincidunt lorem fermentum vitae. Integer ac iaculis mi. Morbi semper est a nibh varius, ac tincidunt nisl hendrerit. Etiam aliquet, neque sit amet eleifend fermentum, nisl massa iaculis arcu, in ornare tellus erat et lorem.</p>
</section>

<form class="application">
  <div class="application-head">Application for Position</div>

  <div class="question" style="top:54px;">
    <div class="q-label">&nbsp;Do you have current Coal Boad Generics</div>
    <div class="text-field"></div>
  </div>
  <div class="divider" style="top:121px;"></div>

  <div class="question" style="top:140px;">
    <div class="q-label">Do you have a current Coal Board Medical.</div>
    <div class="text-field"></div>
  </div>
  <div class="divider" style="top:207px;"></div>

  <div class="question" style="top:226px;">
    <div class="q-label">What mines are you currently inducted at.</div>
    <div class="choices">
      <span class="choice"><i class="box"></i>Ashvale</span>
      <span class="choice"><i class="box"></i>Bluegum</span>
      <span class="choice"><i class="box"></i>Coppercreek</span>
      <span class="choice"><i class="box"></i>Dunmore</span>
      <span class="choice"><i class="box"></i>Emberton</span>
      <span class="choice"><i class="box"></i>Falkner North</span>
      <span class="choice"><i class="box"></i>Falkner 1</span>
      <span class="choice"><i class="box"></i>Glenrock</span>
      <span class="choice"><i class="box"></i>Hartley Downs</span>
    </div>
    <div class="q-note">These are the underground mines in queensland,&nbsp; there will be a list of the underground mines for new south wales as well.</div>
  </div>
  <div class="divider" style="top:288px;"></div>

  <div class="question" style="top:309px;">
    <div class="q-label">What mines have you been inducted at in the past</div>
    <div class="text-field"></div>
  </div>
  <div class="divider" style="top:378px;"></div>

  <div class="question" style="top:396px;">
    <div class="inline-row">
      <div class="q-label">How many years underground experience do you have</div>
      <div class="select-field">1
        <svg width="6" height="9" viewBox="0 0 6 9"><path d="M0 3.5 L3 0.5 L6 3.5 Z M0 5.5 L3 8.5 L6 5.5 Z" fill="#333"/></svg>
      </div>
    </div>
  </div>
  <div class="divider" style="top:435px;"></div>

  <div class="question" style="top:460px;">
    <div class="q-label">What mines are you currently inducted at.</div>
    <div class="choices" style="gap:0 18px;">
      <span class="choice"><i class="box"></i>Shuttle car</span>
      <span class="choice"><i class="box"></i>Quad bolter</span>
      <span class="choice"><i class="box"></i>Air drill</span>
      <span class="choice"><i class="box"></i>LHD loader or similar</span>
      <span class="choice"><i class="box"></i>Wheel loader or similar</span>
      <span class="choice"><i class="box"></i>Personnel carrier</span>
    </div>
  </div>
  <div class="divider" style="top:505px;"></div>

  <div class="question" style="top:525px;">
    <div class="q-label">What qualifications do you currently hold</div>
    <div class="choices" style="gap:0 20px;">
      <span class="choice"><i class="box"></i>Supervisor S1 S2 S3</span>
      <span class="choice"><i class="box"></i>Trade Certificate</span>
      <span class="choice"><i class="box"></i>Deputy Certificate</span>
      <span class="choice"><i class="box"></i>Front line management</span>
      <span class="choice"><i class="box"></i>Trainer and Assessor</span>
    </div>
  </div>
  <div class="divider" style="top:573px;"></div>

  <div class="question" style="top:592px;">
    <div class="q-label">Contact No:</div>
    <div class="phone-row">
      <div class="phone-field" style="width:33px;">+91</div>
      <div class="phone-field" style="width:175px;"></div>
      <div class="phone-field" style="width:175px;"></div>
    </div>
  </div>

  <div class="submit-button">SUBMIT
    <svg width="7" height="7" viewBox="0 0 7 7"><circle cx="3.5" cy="3.5" r="3" fill="#fff"/></svg>
  </div>
</form>

<footer class="site-footer">
  <div class="copyright">© 2014 ironbarkshift.com.au</div>
  <nav class="footer-nav">
    <span>Home</span><span>About Us</span><span>Mission statement</span><span>Contact us</span>
  </nav>
</footer>

</body>
</html>
```